New business card for civil engineering company - "Keystone Audit"

We need a business card designed for our new structural engineering company.

The company name is "Keystone Audit" logo files attached.

We would like the following:
* Two-sided card
* Simple design

Information to be placed on the card:
Name - Marcus Dellow
Job Title - Director / Structural Engineer
Credentials - BEng(Hons), CPEng, CMengNZ, IntPE(NZ)
Email - marcus.dellow@keystoneaudit.co.nz
mobile - 0219364058
website - www.keystoneaudit.co.nz

```html
<!DOCTYPE html>
<html lang="en">
<head>
<meta charset="utf-8">
<title>Keystone Audit — Business Card</title>
<link href="https://fonts.googleapis.com/css2?family=Exo+2:wght@400;600;700&family=Open+Sans:wght@400;600&display=swap" rel="stylesheet">
<style>
  :root {
    --bg: #d8d8d8;
    --card-light: #f2f2f2;
    --card-dark-top: #3a3a3a;
    --card-dark-bottom: #1a1a1a;
    --ink: #1c1c1c;
    --ink-soft: #3e3e3e;
    --bar: #4a4a4a;
    --rule: #5a5a5a;
    --brand-light: #8f8f8f;
  }
  html, body {
    margin: 0;
    padding: 0;
    width: 1200px;
    height: 1083px;
    overflow: hidden;
    background: var(--bg);
  }
  .canvas {
    position: relative;
    width: 1200px;
    height: 1083px;
  }
  .card {
    position: absolute;
    left: 180px;
    width: 840px;
    height: 480px;
    box-shadow: 0 6px 18px rgba(0,0,0,0.18);
    overflow: hidden;
  }
  .card--front { top: 41px; background: var(--card-light); }
  .card--back {
    top: 561px;
    background: linear-gradient(160deg, var(--card-dark-top), var(--card-dark-bottom));
  }

  /* Front */
  .brand {
    position: absolute;
    left: 56px;
    top: 200px;
    display: flex;
    align-items: center;
    gap: 12px;
    font-family: "Exo 2", sans-serif;
    font-weight: 600;
    font-size: 30px;
    letter-spacing: 1px;
    color: var(--ink-soft);
  }
  .brand__mark {
    width: 18px;
    height: 18px;
    background: var(--ink-soft);
  }
  .divider {
    position: absolute;
    left: 330px;
    top: 300px;
    width: 1.5px;
    height: 110px;
    background: var(--rule);
  }
  .identity {
    position: absolute;
    right: 0;
    top: 70px;
    display: flex;
    align-items: flex-start;
  }
  .identity__text {
    text-align: right;
    padding-right: 22px;
  }
  .identity__name {
    font-family: "Exo 2", sans-serif;
    font-weight: 700;
    font-size: 38px;
    color: var(--ink);
    letter-spacing: 1px;
    margin: 0;
    line-height: 1.1;
  }
  .identity__title {
    font-family: "Open Sans", sans-serif;
    font-size: 21px;
    color: var(--ink-soft);
    margin: 4px 0 0;
    letter-spacing: 0.5px;
  }
  .identity__creds {
    font-family: "Open Sans", sans-serif;
    font-weight: 600;
    font-size: 19px;
    color: var(--ink);
    margin: 4px 0 0;
  }
  .identity__bar {
    width: 50px;
    height: 22px;
    margin-top: 12px;
    background: var(--bar);
  }
  .contacts {
    position: absolute;
    left: 372px;
    top: 300px;
    margin: 0;
    padding: 0;
    list-style: none;
    font-family: "Open Sans", sans-serif;
    font-size: 21px;
    color: var(--ink-soft);
  }
  .contacts li {
    display: flex;
    align-items: center;
    gap: 14px;
    height: 38px;
  }
  .contacts svg { width: 18px; height: 18px; flex: none; }
  .contacts .phone { letter-spacing: 4px; }

  /* Back */
  .back-brand {
    position: absolute;
    right: 60px;
    bottom: 60px;
    font-family: "Exo 2", sans-serif;
    font-weight: 600;
    font-size: 54px;
    letter-spacing: 2px;
    color: var(--brand-light);
  }
</style>
</head>
<body>
<main class="canvas">
  <section class="card card--front" aria-label="Business card front">
    <div class="brand"><span class="brand__mark"></span>Keystone Audit</div>
    <div class="divider"></div>

    <div class="identity">
      <div class="identity__text">
        <h1 class="identity__name">Marcus Dellow</h1>
        <p class="identity__title">DIRECTOR / STRUCTURAL ENGINEER</p>
        <p class="identity__creds">BEng(Hons), CPEng, CMengNZ, IntPE(NZ)</p>
      </div>
      <div class="identity__bar"></div>
    </div>

    <ul class="contacts">
      <li>
        <svg viewBox="0 0 18 18" aria-hidden="true"><rect x="1" y="3" width="16" height="12" fill="#3e3e3e"/><path d="M1 3 L9 10 L17 3" fill="none" stroke="#f2f2f2" stroke-width="1.5"/></svg>
        <span>marcus.dellow@keystoneaudit.co.nz</span>
      </li>
      <li>
        <svg viewBox="0 0 18 18" aria-hidden="true"><rect x="5" y="1.5" width="9" height="15" rx="1.5" fill="none" stroke="#3e3e3e" stroke-width="1.3"/></svg>
        <span class="phone">0219364058</span>
      </li>
      <li>
        <svg viewBox="0 0 18 18" aria-hidden="true"><circle cx="9" cy="9" r="7.5" fill="none" stroke="#3e3e3e" stroke-width="1.3"/><ellipse cx="9" cy="9" rx="3.2" ry="7.5" fill="none" stroke="#3e3e3e" stroke-width="1.1"/><line x1="1.5" y1="9" x2="16.5" y2="9" stroke="#3e3e3e" stroke-width="1.1"/></svg>
        <span>www.keystoneaudit.co.nz</span>
      </li>
    </ul>
  </section>

  <section class="card card--back" aria-label="Business card back">
    <div class="back-brand">Keystone Audit</div>
  </section>
</main>
</body>
</html>
```